Re-branding for Structural Engineering firm

We need new business cards as part of our current re-branding. We have a new logo (attached), so the card design should incorporate this color scheme. We are a structural engineering firm providing structural building design and seismic consulting services. The final design should communicate professionalism and stability, with a modern look and feel.

```html
<!DOCTYPE html>
<html lang="en">
<head>
<meta charset="utf-8">
<title>Renwick Structural – Business Card</title>
<link href="https://fonts.googleapis.com/css2?family=Open+Sans:wght@400;700&display=swap" rel="stylesheet">
<style>
  :root {
    --stage: #808083;
    --brand-blue: #1b75bb;
    --brand-gray: #808285;
    --text-gray: #6d6e71;
    --paper: #ffffff;
  }
  * { margin: 0; padding: 0; box-sizing: border-box; }
  html, body { width: 1200px; height: 427px; overflow: hidden; }
  body { background: var(--stage); font-family: "Open Sans", sans-serif; position: relative; }

  .card { position: absolute; width: 477px; height: 267px; background: var(--paper); overflow: hidden; }
  .card--front { left: 104px; top: 94px; }
  .card--back { left: 617px; top: 94px; height: 264px; }

  .card__header { position: absolute; left: 0; top: 0; }
  .card__footer-band { position: absolute; left: 0; bottom: 0; width: 100%; height: 17px; background: var(--brand-blue); }

  .holder { position: absolute; left: 26px; top: 28px; color: var(--paper); }
  .holder__name { font-weight: 700; font-size: 16px; letter-spacing: 0.1px; line-height: 1; }
  .holder__title { font-size: 9px; margin-top: 4px; line-height: 1; }

  .brand { position: absolute; display: flex; flex-direction: column; align-items: center; color: var(--brand-blue); font-weight: 700; text-transform: uppercase; text-align: center; line-height: 1.05; }
  .brand__mark { background: var(--brand-blue); }
  .brand--small { left: 46px; top: 134px; width: 78px; font-size: 8px; }
  .brand--small .brand__mark { width: 46px; height: 46px; margin-bottom: 6px; }
  .brand--large { left: 156px; top: 70px; width: 165px; font-size: 15px; }
  .brand--large .brand__mark { width: 84px; height: 84px; margin-bottom: 10px; }

  .contact { position: absolute; left: 215px; top: 110px; list-style: none; color: var(--text-gray); font-size: 13.5px; line-height: 17px; }
  .contact__item { position: absolute; left: 0; display: flex; align-items: flex-start; white-space: nowrap; }
  .contact__icon { width: 18px; height: 18px; margin-right: 9px; flex: none; }
  .contact__item--address { top: 0; }
  .contact__item--office { top: 41px; }
  .contact__item--mobile { top: 71px; }
  .contact__item--email { top: 104px; }
</style>
</head>
<body>

<section class="card card--front">
  <svg class="card__header" width="477" height="86" viewBox="0 0 477 86">
    <polygon points="0,0 477,0 477,43 296,43 210,86 0,86" fill="var(--brand-blue)"/>
    <polygon points="296,43 477,43 477,50 282,50" fill="var(--brand-gray)"/>
  </svg>

  <div class="holder">
    <p class="holder__name">CAL RENWICK, S.E</p>
    <p class="holder__title">PRINCIPAL</p>
  </div>

  <div class="brand brand--small">
    <span class="brand__mark"></span>
    <span class="brand__name">Renwick Structural</span>
  </div>

  <ul class="contact">
    <li class="contact__item contact__item--address">
      <svg class="contact__icon" viewBox="0 0 18 18"><circle cx="9" cy="9" r="9" fill="var(--text-gray)"/><path d="M9 3.8a3.4 3.4 0 0 0-3.4 3.4c0 2.6 3.4 6.4 3.4 6.4s3.4-3.8 3.4-6.4A3.4 3.4 0 0 0 9 3.8z" fill="#fff"/><circle cx="9" cy="7.2" r="1.3" fill="var(--text-gray)"/></svg>
      <span>4710 Harbor Ridge Dr., Ste 210<br>Corvale, CA 92048</span>
    </li>
    <li class="contact__item contact__item--office">
      <svg class="contact__icon" viewBox="0 0 18 18"><circle cx="9" cy="9" r="9" fill="var(--text-gray)"/><path d="M6.2 4.3l1.6-.3 1 2.4-1.1.9a6 6 0 0 0 2.9 2.9l.9-1.1 2.4 1-.3 1.6c-.2.8-1 1.2-1.8 1C8.4 12 6 9.6 5.3 6.1c-.2-.8.2-1.6.9-1.8z" fill="#fff"/></svg>
      <span>555.214.3870</span>
    </li>
    <li class="contact__item contact__item--mobile">
      <svg class="contact__icon" viewBox="0 0 18 18"><circle cx="9" cy="9" r="9" fill="var(--text-gray)"/><rect x="5.8" y="3.8" width="6.4" height="10.4" rx="1" fill="#fff"/><rect x="6.8" y="5" width="4.4" height="7" fill="var(--text-gray)"/><circle cx="9" cy="13.1" r="0.6" fill="var(--text-gray)"/></svg>
      <span>555.730.4419</span>
    </li>
    <li class="contact__item contact__item--email">
      <svg class="contact__icon" viewBox="0 0 18 18"><circle cx="9" cy="9" r="9" fill="var(--text-gray)"/><rect x="4.6" y="5.8" width="8.8" height="6.4" rx="0.8" fill="none" stroke="#fff" stroke-width="1.2"/><path d="M4.8 6.2L9 9.4l4.2-3.2" fill="none" stroke="#fff" stroke-width="1.2"/></svg>
      <span>cal@renwickse.com</span>
    </li>
  </ul>

  <div class="card__footer-band"></div>
</section>

<section class="card card--back">
  <div class="brand brand--large">
    <span class="brand__mark"></span>
    <span class="brand__name">Renwick Structural</span>
  </div>
</section>

</body>
</html>
```